Vorn Staffing Full Length Retractable Office Banner

I need a design for a full-length retractable banner and A-Frame Sign for each of my offices. I have included designs that have been incorporated into a poster and tri-fold as a sample. I would like to see a colorful eyecatching banner that focuses on people. Would like to see some diversity with men and woman and different races.
Vorn Staffing is a light industrial staffing firm. www.VornStaffing.example

Target Market(s)

Job seekers looking for employment

Industry/Entity Type

Staffing / Recruiting

Font styles to use
Other font styles liked:
• Professional yet fun

Requirements
Must have
• Eye catching design with young hip vibe.
Nice to have
• primary colors with light industrial type jobs

```html
<!DOCTYPE html>
<html lang="en">
<head>
<meta charset="utf-8">
<title>Vorn Staffing Retractable Banner</title>
<link rel="stylesheet" href="https://fonts.googleapis.com/css2?family=Josefin+Sans:wght@300;400&family=Oswald:wght@500;600&family=Roboto:wght@400;700&display=swap">
<style>
  :root {
    --stage: #666666;
    --paper: #ffffff;
    --navy: #2b2a5e;
    --red: #e42521;
    --yellow: #f5df0a;
    --grey-text: #8a8a8a;
    --sky: #eef0f2;
    --crowd-warm: #a08c6e;
    --crowd-deep: #4e4c5e;
    --floor: #f1f2f3;
    --text-light: #ffffff;
  }
  html, body {
    margin: 0;
    width: 1200px;
    height: 930px;
    overflow: hidden;
    background: var(--stage);
  }
  .canvas {
    position: relative;
    width: 1200px;
    height: 930px;
  }
  .banner {
    position: absolute;
    left: 413px;
    top: 25px;
    width: 374px;
    height: 880px;
    display: block;
    box-shadow: 0 6px 18px rgba(0,0,0,0.35);
  }
  .brand-name { font-family: "Josefin Sans", sans-serif; font-weight: 400; fill: var(--navy); }
  .brand-sub { font-family: "Josefin Sans", sans-serif; font-weight: 300; fill: var(--grey-text); }
  .headline-condensed { font-family: "Oswald", sans-serif; fill: var(--text-light); }
  .headline-sans { font-family: "Roboto", sans-serif; fill: var(--text-light); }
  .hiring { font-family: "Oswald", sans-serif; font-weight: 600; fill: var(--yellow); }
  .web-address { font-family: "Roboto", sans-serif; font-weight: 400; fill: var(--text-light); }
</style>
</head>
<body>
<main class="canvas">
  <svg class="banner" viewBox="0 0 439 1035" xmlns="http://www.w3.org/2000/svg" aria-label="Vorn Staffing roll-up banner">
    <defs>
      <linearGradient id="crowd-tones" x1="0" y1="0" x2="0" y2="1">
        <stop offset="0" stop-color="var(--paper)"/>
        <stop offset="0.22" stop-color="var(--sky)"/>
        <stop offset="0.45" stop-color="var(--crowd-warm)"/>
        <stop offset="0.68" stop-color="var(--crowd-deep)"/>
        <stop offset="0.88" stop-color="var(--floor)"/>
        <stop offset="1" stop-color="var(--floor)"/>
      </linearGradient>
    </defs>

    <rect class="banner-ground" x="0" y="0" width="439" height="1035" fill="var(--paper)"/>

    <g class="brand-lockup">
      <circle class="brand-dot" cx="78" cy="150" r="14" fill="var(--red)"/>
      <text class="brand-name" x="105" y="180" font-size="140" textLength="268" lengthAdjust="spacingAndGlyphs">Vorn</text>
      <text class="brand-sub" x="368" y="214" font-size="36" text-anchor="end">staffing</text>
    </g>

    <rect class="team-photo" role="img" aria-label="Photo of a diverse group of smiling men and women standing together in front of a bright city skyline" x="0" y="232" width="439" height="360" fill="url(#crowd-tones)"/>

    <polygon class="message-band" points="0,585 439,510 439,1035 0,1035" fill="var(--navy)"/>

    <g class="message">
      <text class="headline-condensed" x="48" y="658" font-size="78" font-weight="600" textLength="344" lengthAdjust="spacingAndGlyphs">CONNECTING</text>
      <text class="headline-sans" x="50" y="711" font-size="50" textLength="340" lengthAdjust="spacingAndGlyphs"><tspan font-weight="700">GREAT</tspan> PEOPLE</text>
      <text class="headline-sans" x="220" y="747" font-size="30" text-anchor="middle">WITH</text>
      <text class="headline-condensed" x="50" y="794" font-size="46" font-weight="500" textLength="342" lengthAdjust="spacingAndGlyphs">GREAT ORGANIZATIONS!</text>
      <line class="divider" x1="52" y1="816" x2="387" y2="816" stroke="var(--text-light)" stroke-width="1"/>
      <rect class="divider-accent" x="197" y="814" width="46" height="5" fill="var(--yellow)"/>
      <text class="hiring" x="43" y="881" font-size="64" textLength="356" lengthAdjust="spacingAndGlyphs">ALWAYS HIRING</text>
    </g>

    <polygon class="footer-band" points="0,970 439,895 439,1035 0,1035" fill="var(--red)"/>
    <text class="web-address" x="220" y="996" font-size="20" text-anchor="middle" textLength="322" lengthAdjust="spacing">www.VornStaffing.example</text>
  </svg>
</main>
</body>
</html>
```